Web SITE design for new book

I need a unique design for a book my friend is releasing.

The home page needs to include:
A picture of the book
A spot for a video

Navigation:
Home
About the Book
Buy the Book
About the Author
Investing
Log In

The person awarded the project will also need to provide designs for the 5 other internal pages. They should be pretty straight forward.

Link to book design: https://www.filvantra.net/s/qmrt82kw7zpalvq/book-cover.png

Thanks!

```html
<!DOCTYPE html>
<html lang="en">
<head>
<meta charset="utf-8">
<title>Book Home Page</title>
<link rel="stylesheet" href="https://fonts.googleapis.com/css2?family=Open+Sans:wght@400;600&family=Raleway:wght@400;500&display=swap">
<style>
  :root {
    --gold: #a88f4e;
    --orange: #ff5a00;
    --black: #000000;
    --ink: #111111;
    --muted: #6b6b6b;
    --white: #ffffff;
    --hero-light: #f6f6f5;
    --hero-mid: #e4e3df;
    --bar: #1e2124;
  }
  * { margin: 0; padding: 0; box-sizing: border-box; }
  html, body { width: 1200px; height: 810px; overflow: hidden; background: var(--white); }
  body { position: relative; font-family: "Open Sans", Arial, sans-serif; color: var(--ink); }

  .contact-line { position: absolute; top: 6px; right: 188px; font-size: 13px; color: var(--ink); }

  .nav-band { position: absolute; top: 30px; left: 0; width: 1200px; height: 51px; background: var(--gold); }
  .main-nav { position: absolute; top: 30px; left: 0; width: 880px; height: 51px; }
  .main-nav a { position: absolute; top: 0; line-height: 51px; white-space: nowrap; font-family: "Raleway", Arial, sans-serif;
    font-size: 14px; color: var(--white); text-decoration: none; }
  .nav-home { left: 324px; }
  .nav-about-book { left: 386px; }
  .nav-buy { left: 503px; }
  .nav-author { left: 608px; }
  .nav-investing { left: 736px; }
  .nav-login { left: 813px; }
  .order-button { position: absolute; top: 30px; left: 881px; width: 131px; height: 51px; background: var(--orange);
    color: var(--white); font-family: "Raleway", Arial, sans-serif; font-size: 17px; display: flex; align-items: center; justify-content: center; text-decoration: none; }

  .brand-tab { position: absolute; top: 30px; left: 187px; width: 87px; height: 121px; z-index: 3; }
  .brand-name { position: absolute; top: 41px; left: 187px; width: 87px; z-index: 4; text-align: center;
    font-size: 20px; line-height: 18px; color: var(--ink); }
  .brand-name .mark { display: block; width: 26px; height: 26px; border-radius: 50%; background: var(--gold); margin: 0 auto 13px; }

  .hero-backdrop { position: absolute; top: 81px; left: 0; width: 1200px; height: 379px;
    background: linear-gradient(180deg, var(--white) 0%, var(--hero-light) 35%, var(--hero-mid) 100%); }
  .hero-copy { position: absolute; top: 195px; left: 187px; width: 370px; }
  .hero-copy h1 { font-weight: 400; font-size: 18px; line-height: 22px; }
  .points { list-style: none; margin-top: 10px; }
  .points li { display: flex; align-items: center; gap: 5px; font-size: 14px; height: 27px; white-space: nowrap; }
  .points svg { flex: none; }
  .actions { position: absolute; top: 390px; left: 187px; display: flex; gap: 7px; }
  .btn { height: 45px; display: flex; align-items: center; justify-content: center; font-family: "Raleway", Arial, sans-serif;
    font-size: 17px; color: var(--white); text-decoration: none; }
  .btn-gold { width: 134px; background: var(--gold); }
  .btn-dark { width: 171px; background: var(--black); }

  .media-band { position: absolute; top: 460px; left: 0; width: 1200px; height: 184px; background: var(--black); }
  .video-player { position: absolute; top: 481px; left: 187px; width: 205px; height: 140px; }
  .video-still { width: 205px; height: 116px; background: linear-gradient(135deg, #dfe4e6 0%, #e8c25a 55%, #b98d3a 100%); }
  .video-bar { display: block; width: 205px; height: 24px; background: var(--bar); }

  .book-art { position: absolute; top: 128px; left: 640px; z-index: 2; }

  .site-footer { position: absolute; top: 679px; left: 0; width: 1200px; text-align: center; }
  .footer-nav { font-size: 12px; color: var(--muted); }
  .footer-nav a { color: var(--muted); text-decoration: none; }
  .footer-nav span { margin: 0 5px; }
  .copyright { margin-top: 11px; font-size: 12px; color: var(--muted); }
  .social { margin-top: 20px; display: flex; justify-content: center; gap: 5px; }
  .social a { width: 29px; height: 29px; border: 2px solid #9a9a9a; border-radius: 50%; display: block; }
</style>
</head>
<body>
  <p class="contact-line">Call us for Order : 1800 555 0142</p>

  <div class="nav-band"></div>
  <svg class="brand-tab" width="87" height="121" viewBox="0 0 87 121">
    <defs><linearGradient id="tabFill" x1="0" y1="0" x2="0" y2="1"><stop offset="0" stop-color="#ffffff"/><stop offset="1" stop-color="#e6e6e6"/></linearGradient></defs>
    <polygon points="0,0 87,0 87,121 43.5,106 0,121" fill="url(#tabFill)"/>
  </svg>
  <div class="brand-name"><span class="mark"></span>Logo<br>Here</div>

  <nav class="main-nav">
    <a class="nav-home" href="#">Home</a>
    <a class="nav-about-book" href="#">About the Book</a>
    <a class="nav-buy" href="#">Buy the Book</a>
    <a class="nav-author" href="#">About the Author</a>
    <a class="nav-investing" href="#">Investing</a>
    <a class="nav-login" href="#">LogIn</a>
  </nav>
  <a class="order-button" href="#">Order Now</a>

  <div class="hero-backdrop" role="img" aria-label="Faint background photo of banknotes"></div>
  <section class="hero-copy">
    <h1>Lorem ipsum dolor sit amet, consectetur adipiscing elit. In fermentum dolor non augue pretium egestas.</h1>
    <ul class="points">
      <li><svg width="16" height="16" viewBox="0 0 16 16"><circle cx="8" cy="8" r="7" fill="none" stroke="#111" stroke-width="1.4"/><rect x="7.2" y="3.5" width="1.6" height="6" fill="#111"/><rect x="7.2" y="10.8" width="1.6" height="1.6" fill="#111"/></svg>Fermentum dolor non augue pretium egestas.</li>
      <li><svg width="16" height="16" viewBox="0 0 16 16"><circle cx="8" cy="8" r="7" fill="none" stroke="#111" stroke-width="1.4"/><rect x="7.2" y="3.5" width="1.6" height="6" fill="#111"/><rect x="7.2" y="10.8" width="1.6" height="1.6" fill="#111"/></svg>Lorem ipsum dolor sit amet</li>
      <li><svg width="16" height="16" viewBox="0 0 16 16"><circle cx="8" cy="8" r="7" fill="none" stroke="#111" stroke-width="1.4"/><rect x="7.2" y="3.5" width="1.6" height="6" fill="#111"/><rect x="7.2" y="10.8" width="1.6" height="1.6" fill="#111"/></svg>Consectetur adipiscing elit fermentum</li>
    </ul>
  </section>
  <div class="actions">
    <a class="btn btn-gold" href="#">Learn More</a>
    <a class="btn btn-dark" href="#">Learn Investing</a>
  </div>

  <div class="media-band"></div>
  <div class="video-player">
    <div class="video-still" role="img" aria-label="Video still of a man building a bar chart on a desk"></div>
    <svg class="video-bar" width="205" height="24" viewBox="0 0 205 24">
      <circle cx="13" cy="12" r="6.5" fill="none" stroke="#fff" stroke-width="1.2"/>
      <polygon points="11,9 11,15 16,12" fill="#fff"/>
      <line x1="26" y1="0" x2="26" y2="24" stroke="#000" stroke-width="1"/>
      <rect x="36" y="11" width="140" height="3" rx="1.5" fill="#0d0f10"/>
      <rect x="36" y="11" width="45" height="3" rx="1.5" fill="#5a8fb8"/>
      <circle cx="72" cy="12.5" r="3.5" fill="#fff"/>
      <g fill="#3aa0e0"><rect x="183" y="10" width="1.2" height="5"/><rect x="185.5" y="10" width="1.2" height="5"/><rect x="188" y="10" width="1.2" height="5"/><rect x="190.5" y="10" width="1.2" height="5"/><rect x="193" y="10" width="1.2" height="5"/></g>
    </svg>
  </div>

  <svg class="book-art" width="350" height="485" viewBox="0 0 350 485" role="img" aria-label="Hardcover of the book standing at an angle">
    <defs><linearGradient id="coverFill" x1="0" y1="0" x2="1" y2="1"><stop offset="0" stop-color="#ffffff"/><stop offset="1" stop-color="#dcdcdc"/></linearGradient></defs>
    <polygon points="316,12 344,12 326,432 298,478" fill="#1a1a1a"/>
    <polygon points="312,14 320,14 302,470 294,476" fill="#d8d8d8"/>
    <polygon points="12,8 316,14 298,478 28,410" fill="url(#coverFill)"/>
  </svg>

  <footer class="site-footer">
    <nav class="footer-nav">
      <a href="#">Home</a><span>/</span><a href="#">About the Book</a><span>/</span><a href="#">Buy the Book</a><span>/</span><a href="#">About the Author</a><span>/</span><a href="#">Investing</a><span>/</span><a href="#">LogIn</a><span>/</span><a href="#">Terms</a>
    </nav>
    <p class="copyright">Copyright © 2014</p>
    <div class="social"><a href="#" aria-label="Social profile"></a><a href="#" aria-label="Social profile"></a></div>
  </footer>
</body>
</html>
```